Website Design for Car Donations

Revise current site www.ridesforhonor.org

Sites i like:

https://www.wheelsformilitary.org

https://autogivingforheroes.org

https://plinkmock.com/144490c6/screen/39053423

Coding

Coded - Design and coding required

Number of Pages Required

1 page

```html
<!DOCTYPE html>
<html lang="en">
<head>
<meta charset="utf-8">
<title>Rides For Honor – Donate Your Car</title>
<link rel="stylesheet" href="https://fonts.googleapis.com/css2?family=Poppins:wght@400;500;600;700&family=Open+Sans:ital,wght@0,400;0,600;1,400&display=swap">
<style>
:root{
  --red:#c8102e;
  --navy:#1f3f8f;
  --blue-deep:#1a3a8a;
  --ink:#1c1c1c;
  --muted:#555;
  --field:#eeeeee;
  --line:#d8d8d8;
  --grey-band:#e4e4e4;
  --footer:#262626;
  --footer-dark:#161616;
  --white:#fff;
}
*{box-sizing:border-box;margin:0;padding:0}
html,body{width:1200px;height:3120px;overflow:hidden}
body{position:relative;font-family:"Poppins",sans-serif;color:var(--ink);background:var(--white)}
.abs{position:absolute}

/* header */
.site-header{position:absolute;top:0;left:0;width:1200px;height:88px;background:var(--white)}
.brand{position:absolute;left:104px;top:22px;display:flex;align-items:center;gap:10px;font-weight:700;font-size:26px;color:var(--red);text-transform:uppercase}
.brand-mark{width:34px;height:34px;background:var(--red);border-radius:50%}
.main-nav{position:absolute;left:510px;top:30px;display:flex;gap:0}
.main-nav a{font-size:15px;color:var(--ink);text-decoration:none;margin-right:46px}
.btn-donate-top{position:absolute;left:960px;top:24px;width:140px;height:40px;background:var(--red);color:var(--white);font-size:13px;font-weight:500;display:flex;align-items:center;justify-content:center;text-transform:uppercase}

/* hero */
.hero{position:absolute;top:88px;left:0;width:1200px;height:492px;background:linear-gradient(100deg,#5b6a3c 0%,#7c8a58 30%,#9aa27a 55%,#b5b29a 75%,#8e7e62 100%)}
.hero-copy{position:absolute;left:0;top:140px;width:730px;text-align:center;color:var(--white)}
.hero-copy .t1{font-size:33px;font-weight:500}
.hero-copy .t2{font-size:40px;font-weight:600;margin-top:2px}
.hero-copy .phone{font-size:50px;font-weight:700;color:var(--red);letter-spacing:1px;margin-top:0}
.hero-copy .t3{font-size:18px;font-weight:500;margin-top:4px}
.slider-dots{position:absolute;left:565px;top:448px;display:flex;gap:6px}
.slider-dots span{width:14px;height:14px;border-radius:50%;background:var(--white)}
.slider-dots span.active{background:var(--red)}

/* donate section */
.donate{position:absolute;top:580px;left:0;width:1200px;height:690px;background:var(--white)}
.donate-scene{position:absolute;left:0;top:280px;width:1200px;height:410px;background:linear-gradient(180deg,#fff 0%,#ececec 40%,#d4d4d4 100%)}
.form-card{position:absolute;left:100px;top:90px;width:412px;height:530px;background:var(--white);border:1px solid #ddd;border-radius:8px;box-shadow:0 4px 14px rgba(0,0,0,.12);padding:28px 18px}
.form-card h2{text-align:center;color:var(--navy);font-size:26px;font-weight:600;margin-bottom:22px}
.field{height:42px;background:var(--field);border:1px solid var(--line);font-size:12px;color:#444;padding:0 18px;display:flex;align-items:center;margin-bottom:10px;font-family:"Open Sans",sans-serif}
.field-row{display:flex;gap:8px}
.field-row .field{flex:1;justify-content:space-between}
.caret{width:0;height:0;border-left:6px solid transparent;border-right:6px solid transparent;border-top:7px solid #333}
.btn-submit-form{height:44px;background:var(--red);border-radius:6px;color:var(--white);font-weight:600;font-size:17px;display:flex;align-items:center;justify-content:center;margin-top:12px}
.benefits{position:absolute;left:565px;top:80px;width:560px}
.benefits h2{font-size:34px;font-weight:500;line-height:44px}
.benefit-grid{display:grid;grid-template-columns:275px 275px;row-gap:26px;margin-top:30px}
.benefit{display:flex;gap:16px;align-items:flex-start;font-size:17px;line-height:24px}
.benefit svg{flex:none}

/* why */
.why{position:absolute;top:1270px;left:0;width:1200px;height:525px;background:linear-gradient(180deg,#1c3a8c 0%,#2a55b5 45%,#1d3d8e 100%);color:var(--white)}
.why h2{position:absolute;top:62px;width:1200px;text-align:center;font-size:34px;font-weight:500}
.why-list{position:absolute;left:110px;top:150px;width:1010px;list-style:none}
.why-list li{position:relative;padding-left:46px;font-size:16px;line-height:28px;margin-bottom:23px}
.why-list li b{font-weight:600}
.why-list li::before{content:"⟶";position:absolute;left:0;top:0;font-size:22px}

/* how */
.how{position:absolute;top:1795px;left:0;width:1200px;height:515px;background:var(--white)}
.how h2{position:absolute;top:80px;width:1200px;text-align:center;font-size:34px;font-weight:500}
.step{position:absolute;top:170px;width:360px;text-align:center}
.step-icon{width:136px;height:136px;margin:0 auto;border-radius:50%;border:3px solid var(--navy);display:flex;align-items:center;justify-content:center;box-shadow:inset 0 0 0 10px #fff,inset 0 0 0 11px #eee}
.step h3{font-size:20px;font-weight:600;margin-top:22px}
.step p{font-family:"Open Sans",sans-serif;font-size:13px;line-height:24px;color:#333;margin-top:8px;padding:0 40px}

/* testimonials */
.testimonials{position:absolute;top:2310px;left:0;width:1200px;height:400px;background:linear-gradient(180deg,#f2f2f2 0%,#e0e0e0 55%,#c8c8c8 100%)}
.testimonials h2{position:absolute;top:70px;width:1200px;text-align:center;font-size:34px;font-weight:500}
.quote{position:absolute;top:160px;width:430px;font-family:"Open Sans",sans-serif;font-style:italic;font-size:13px;line-height:26px;color:#333}
.quote cite{display:block;font-style:normal;font-family:"Poppins",sans-serif;font-weight:600;color:var(--navy);font-size:14px;margin-top:10px}
.quote-mark{position:absolute;left:540px;top:175px;width:120px;height:120px;border-radius:50%;background:var(--white);box-shadow:0 0 0 12px rgba(255,255,255,.5);display:flex;align-items:center;justify-content:center;color:var(--red);font-size:90px;font-weight:700;line-height:1;font-family:"Poppins",sans-serif}

/* footer */
.site-footer{position:absolute;top:2710px;left:0;width:1200px;height:350px;background:var(--footer);color:var(--white)}
.site-footer h4{font-size:18px;font-weight:500;margin-bottom:28px}
.footer-col{position:absolute;top:62px}
.footer-col p{font-size:12px;line-height:26px;color:#e6e6e6}
.footer-col a{display:block;font-size:12px;color:#e6e6e6;text-decoration:none;line-height:27px}
.badge{position:absolute;background:#555;border-radius:6px}
.news-field{font-size:12px;color:#e6e6e6;border-bottom:1px solid #999;width:262px;padding-bottom:6px;margin-bottom:18px}
.btn-submit-news{position:absolute;left:1003px;top:192px;width:92px;height:30px;background:var(--red);font-size:14px;font-weight:600;display:flex;align-items:center;justify-content:center;text-transform:uppercase;border-radius:3px}
.socials{position:absolute;left:880px;top:252px;display:flex;gap:12px}
.socials span{width:46px;height:46px;border-radius:50%;background:var(--white);display:flex;align-items:center;justify-content:center}
.socials span i{width:16px;height:16px;border-radius:50%;background:var(--red);display:block}
.copyright{position:absolute;top:3060px;left:0;width:1200px;height:60px;background:var(--footer-dark);color:#ddd;font-size:12px;display:flex;align-items:center;justify-content:center}
</style>
</head>
<body>

<header class="site-header">
  <div class="brand"><span class="brand-mark"></span>Rides For Honor</div>
  <nav class="main-nav">
    <a href="#">How To Donate</a><a href="#">Why Donate</a><a href="#">FAQ</a><a href="#">About</a>
  </nav>
  <div class="btn-donate-top">Donate Now</div>
</header>

<section class="hero" role="img" aria-label="Soldier in camouflage embracing a smiling child holding a small American flag, outdoors">
  <div class="hero-copy">
    <div class="t1">Donate Your Cars To Veterans</div>
    <div class="t2">CALL TODAY TO DONATE</div>
    <div class="phone">1-800-555-0142</div>
    <div class="t3">Live Operators Available - 7 Days A Week</div>
  </div>
  <div class="slider-dots"><span></span><span></span><span></span><span class="active"></span></div>
</section>

<section class="donate">
  <div class="donate-scene" role="img" aria-label="Faint grey silhouettes of soldiers in the field against hills"></div>
  <form class="form-card">
    <h2>Donate Your Car Online</h2>
    <div class="field">First Name</div>
    <div class="field">Last Name</div>
    <div class="field">Email</div>
    <div class="field">Phone</div>
    <div class="field">Zip Code</div>
    <div class="field-row">
      <div class="field">Choose Year<span class="caret"></span></div>
      <div class="field">Choose Make<span class="caret"></span></div>
    </div>
    <div class="field">Vehicle Model</div>
    <div class="btn-submit-form">DONATE NOW !</div>
  </form>
  <div class="benefits">
    <h2>Donate Your Car To Make A Difference</h2>
    <div class="benefit-grid">
      <div class="benefit"><svg width="42" height="42" viewBox="0 0 42 42" fill="none" stroke="#1f3f8f" stroke-width="2.5"><circle cx="21" cy="21" r="17"/><path d="M26 15h-7a3 3 0 0 0 0 6h4a3 3 0 0 1 0 6h-7M21 11v4M21 27v4"/></svg><span>You have No<br>Costs</span></div>
      <div class="benefit"><svg width="42" height="42" viewBox="0 0 42 42" fill="none" stroke="#1f3f8f" stroke-width="2.5"><path d="M6 28V18h14v10M20 22h8l5 6v0H20"/><circle cx="12" cy="31" r="3"/><circle cx="28" cy="31" r="3"/><path d="M8 18l6-10" stroke="#c8102e"/></svg><span>Free Towing,<br>Running Or Not</span></div>
      <div class="benefit"><svg width="42" height="42" viewBox="0 0 42 42" fill="none" stroke="#1f3f8f" stroke-width="2.5"><rect x="8" y="5" width="22" height="30" rx="2"/><path d="M13 13h12M13 19h12M13 25h6"/><circle cx="30" cy="30" r="6" stroke="#c8102e"/></svg><span>We Issue You An<br>IRS Tax Receipt</span></div>
      <div class="benefit"><svg width="42" height="42" viewBox="0 0 42 42" fill="none" stroke="#1f3f8f" stroke-width="2.5"><rect x="9" y="6" width="24" height="30" rx="2" transform="rotate(10 21 21)"/><path d="M15 15h12M14 21h12M13 27h8"/></svg><span>We Take Care Of<br>All Paperwork</span></div>
      <div class="benefit"><svg width="42" height="42" viewBox="0 0 42 42" fill="none" stroke="#1f3f8f" stroke-width="2.5"><rect x="4" y="9" width="34" height="24" rx="2"/><circle cx="15" cy="19" r="4"/><path d="M9 28c1-4 11-4 12 0M24 17h9M24 23h9" stroke="#c8102e"/></svg><span>No DMV Hassles</span></div>
      <div class="benefit"><svg width="42" height="42" viewBox="0 0 42 42" fill="none" stroke="#1f3f8f" stroke-width="2.5"><rect x="4" y="11" width="34" height="20" rx="2"/><path d="M14 11v20" stroke-dasharray="3 3"/><path d="M22 17l8 8M30 17l-8 8" stroke="#c8102e"/></svg><span>Vacation Voucher</span></div>
    </div>
  </div>
</section>

<section class="why" role="img" aria-label="Soldier silhouette walking against a blue sky over a waving flag">
  <h2>Why Donate Your Car To Us</h2>
  <ul class="why-list">
    <li><b>IRS 501(c)3 Approved :</b> Free 24/7 Pickup with No DMV Hassles.</li>
    <li><b>Free Local Towing :</b> We will pick up your car donation, running or not, when it's most convenient,<br>at home or work.</li>
    <li><b>Income Tax Deduction :</b> We issue you an IRS tax receipt and get you the highest tax write-off possible.</li>
    <li><b>No Paperwork Hassles :</b> We handle everything: DMV and IRS paperwork.</li>
    <li><b>Car donations help fund programs :</b> And benefit Valor Path Foundation. An IRS 501(c)3 nonprofit organization.</li>
    <li><b>Schedule a Free Pickup :</b> Complete the form and a representative will call you to arrange a convenient time<br>to pickup your car.</li>
  </ul>
</section>

<section class="how">
  <h2>How Car Donation Works</h2>
  <div class="step" style="left:78px">
    <div class="step-icon"><svg width="52" height="52" viewBox="0 0 52 52" fill="none" stroke="#c8102e" stroke-width="3" stroke-linejoin="round"><path d="M14 6l8 9-4 5c2 6 7 11 13 13l5-4 9 8-5 6C24 45 7 28 8 12z"/><path d="M31 8a14 14 0 0 1 13 13M30 15a7 7 0 0 1 7 7"/></svg></div>
    <h3>1. Contact Us</h3>
    <p>Donating your vehicle is easy &amp; donation is accepted nationwide.</p>
  </div>
  <div class="step" style="left:420px">
    <div class="step-icon"><svg width="58" height="52" viewBox="0 0 58 52" fill="none" stroke-width="3"><path d="M6 36V24h20v12M26 28h14l8 8H26" stroke="#c8102e" fill="#c8102e"/><circle cx="14" cy="40" r="5" stroke="#1f3f8f" fill="#fff"/><circle cx="38" cy="40" r="5" stroke="#1f3f8f" fill="#fff"/><path d="M10 24l14-16M24 8v10" stroke="#1f3f8f"/></svg></div>
    <h3>2. We Tow The Vehicle</h3>
    <p>Any vehicles are accepted and we will arrange to pick up your vehicle when it is most convenient for you.</p>
  </div>
  <div class="step" style="left:764px">
    <div class="step-icon"><svg width="50" height="54" viewBox="0 0 50 54" fill="none" stroke="#c8102e" stroke-width="3"><rect x="8" y="4" width="28" height="38" rx="2"/><path d="M14 14h16M14 21h16M14 28h8"/><circle cx="36" cy="40" r="8" fill="#fff"/><path d="M32 40h8"/></svg></div>
    <h3>3. TAX WRITE-OFF</h3>
    <p>Once the vehicle donation is complete, you will receive your tax deductable vehicle donation receipt.</p>
  </div>
</section>

<section class="testimonials" role="img" aria-label="Grey silhouette of a soldier with hills behind">
  <h2>What Our Donors Are Saying?</h2>
  <blockquote class="quote" style="left:100px">" Lorem ipsum dolor sit amet, consectetur adipiscing elit, sed do eiusmod tempor incididunt ut labore et dolore magna aliqua. Ut enim ad minim veniam, quis nostrud exercitation ullamco laboris nisi ut aliquip ex ea commodo consequat. "<cite>– Dana Whitfield, Sedan Donor - California</cite></blockquote>
  <div class="quote-mark">“</div>
  <blockquote class="quote" style="left:692px">" Lorem ipsum dolor sit amet, consectetur adipiscing elit, sed do eiusmod tempor incididunt ut labore et dolore magna aliqua. Ut enim ad minim veniam, quis nostrud exercitation ullamco laboris nisi ut aliquip ex ea commodo consequat. "<cite>– Dana Whitfield, Sedan Donor - California</cite></blockquote>
</section>

<footer class="site-footer">
  <div class="footer-col" style="left:100px;width:400px">
    <h4>About Us</h4>
    <p>Car donations help fund programs and benefit Valor Path Foundation. An IRS 501(c)3 nonprofit organization. Schedule a Free Pickup: Complete the form and a representative will call you to arrange a convenient time to pickup your car.</p>
  </div>
  <div class="badge" style="left:100px;top:237px;width:150px;height:56px"></div>
  <div class="badge" style="left:282px;top:237px;width:72px;height:56px;border-radius:50%"></div>
  <div class="footer-col" style="left:576px">
    <h4>Navigation Links</h4>
    <a href="#">How To Donate</a><a href="#">Why Donate</a><a href="#">FAQ</a><a href="#">About</a>
  </div>
  <div class="footer-col" style="left:833px">
    <h4>Newsletter Subscription</h4>
    <div class="news-field">Name</div>
    <div class="news-field">Email</div>
  </div>
  <div class="btn-submit-news">Submit</div>
  <div class="socials"><span><i></i></span><span><i></i></span><span><i></i></span><span><i></i></span></div>
</footer>
<div class="copyright">Copyright © 2018. All Rights Reserved.</div>

</body>
</html>
```